Bottle labels and logo for small distillery

Harbor Stillhouse is a small beginning project of handcrafted distillery producing cider spirit (same as apple wine spirit) and apple vodka from apple wine. There are not many similar small distilleries in the Baltic Sea region and very few of them produce apple brandy, so the concept and the product itself are unique. That is the reason we are not developing any distinctive brand and we are sticking to two elements – company name ‘Harbor Stillhouse OÜ’ and product name ‘Orchardine’. Best branding solution for us would be to have a clear logo instead of words.

In the future it is most likely that the product range will broaden by some type of sweet liqueurs like apple-liqueur and black-currant-liqueur and both will be mixtures of natural juice and apple brandy.

We have tested the product itself and more or less chosen proper bottle and closing. Example of the shape of the bottle:

https://www.vessel-depot.example.co.uk/Glass-vessels/Glass-vessels/500ml-glass-vessels/500ml-clear-glass-vessel-Rondel.html

Sizes of bottles:
500 ml Height (without cap) 350 mm, external diameter 60 mm;
375 ml Height (without cap) 330 mm, external diameeter 55 mm;

The bottle cap/closing is going to be waxed, and should look something like that:

http://img.picstash-example.com/qR7Tz.jpg

The design has two separate parts: (1) paper bottle label and (2) print on the bottle.

Front side – printed to the bottle, preferably a symbol without text, for better quality of print rather a vector graphics (monochrome or up to 3-single colour picture). We would like to use the symbol also as an enterprise logo if possible (but logo and bottle print can also be different if designer decides so). It should give a hint to apple based distillate (but, we do not want to narrow down creators fantasy so if you have a good idea please don’t hold back). Just to offer a dumb examples:
https://moodbinder-example.com/entry/51839206
https://www.pinboardly-example.ca/pin/719302846615902418/?lp=true https://www.stockframe-example.com/image-vector/decorative-apple-flora-ornaments-leaf-flower-482017356?src=QXP_tbRkLw8YpH3JcV_29m-2-50
NB! these are just examples of style, contents are more or less random.

Back side – a rectangular shaped label glued to the bottle. Label should not be a square but rather oblong and narrow. The colour of the label shouldn’t be white but rather light yellow, light brown or light creamy. Some examples:

https://www.pinboardly-example.co.uk/pin/830174529266108354 https://www.pinboardly-example.co.uk/pin/591840372605183924

Label has to contain such information:
1) (Product in large print) Orchardine
2) (product) apple wine spirit
3) (Neto amount) 50 cl; / 35 cl
4) (Ethanol in large print) 45%; / 55%
5) (Producer) Produced by Harbor Stillhouse, Lõunamaa 48213, Rannaküla, Sõstra 7;
6) (raw material and technology) Made in Estonia. Product is made of Estonian apple wine and distilled in reflux still in small batches
7) (distillate) Distillate 85%
8) (batch no) Batch no: (stamp) …
9) (note) produced with utmost pleasure
10) (note) Consume responsibly
11) (signature) distiller: …

We also need the label to be designed in Estonian as follows:
1) Orchardine
2) Õunaveini destillaat
3) 50 cl; / 35 cl
4) 45% / 55%
5) Toodetud Harbor Stillhouse OÜ poolt, Lõunamaal 48213, Rannaküla, Sõstra 7;
6) Toodetud Eestis, eestimaisest õunaveinist ja destilleeritud käsitööna väikeste partiidena
7) Destillaat 85%
8) Partii nr:
9) Toodetud puhtast rõõmust
10) Tarbige vastutustundlikult!
11) Meister:

Design as such can be the same. Since we are planning to bottle the product in 375 ml and 500 ml bottles and dilute it down to 45% and 55%. So, there should be 37,5 cl 45%, 50 cl 45%; 37,5 cl 55%; 50 cl 55%.

We assume that in case of 37,5 cl and 50 cl bottles we can use the same design and just resize the printed image and paper-label a bit.

Since the product is handmade and high quality we would like to stress credibility. Not as important as the first purchase is the second purchase of clients – the label should not be shocking but rather trustworthy. And classy in the very best sense.

We are hoping to have a long term business relationship with possible future designer.

Target Market(s)

Adult male alcohol consumers

Industry/Entity Type

Food Production

Logo Text

Harbor Stillhouse

Colors

Designer to choose colors to be used in the design.

```html
<!DOCTYPE html>
<html lang="en">
<head>
<meta charset="utf-8">
<title>Orchardine – Harbor Stillhouse front label</title>
<link rel="stylesheet" href="https://fonts.googleapis.com/css2?family=Arimo:wght@700&family=Libre+Baskerville:wght@400&family=Pinyon+Script&family=Yellowtail&display=swap">
<style>
  :root {
    --label-black: #1d1b1b;
    --paper-white: #ffffff;
    --gold: #b8873c;
    --gold-light: #e2b862;
    --canvas: #ffffff;
  }
  html, body {
    margin: 0;
    padding: 0;
    width: 1200px;
    height: 1200px;
    overflow: hidden;
    background: var(--canvas);
  }
  .label-stage {
    width: 1200px;
    height: 1200px;
    display: flex;
    align-items: center;
    justify-content: center;
  }
  .bottle-label { width: 1000px; height: auto; display: block; }

  .label-body { fill: var(--label-black); }
  .frame-white { fill: none; stroke: var(--paper-white); stroke-width: 5; }
  .frame-gold { fill: none; stroke: var(--gold); stroke-width: 3; }
  .frame-dots { fill: none; stroke: var(--paper-white); stroke-width: 2.6; stroke-dasharray: 0.1 6; stroke-linecap: round; }

  .ribbon-tail { fill: var(--label-black); }
  .ribbon-tail-line { fill: none; stroke: var(--gold); stroke-width: 2.5; }
  .ribbon-band { fill: var(--label-black); stroke: var(--paper-white); stroke-width: 5; }
  .ribbon-gold { fill: none; stroke: var(--gold); stroke-width: 3; }

  .tag-ends { fill: var(--gold); }
  .tag-box { fill: var(--paper-white); }
  .tag-text {
    font-family: "Arimo", Arial, sans-serif;
    font-weight: 700;
    font-size: 22px;
    fill: var(--label-black);
  }
  .product-name {
    font-family: "Yellowtail", cursive;
    font-size: 108px;
    fill: var(--paper-white);
    stroke: var(--gold);
    stroke-width: 1.4;
    paint-order: stroke;
  }
  .tagline {
    font-family: "Pinyon Script", cursive;
    font-size: 30px;
    fill: var(--gold);
  }
  .established {
    font-family: "Libre Baskerville", Georgia, serif;
    font-size: 27px;
    fill: var(--paper-white);
  }
  .maker-name {
    font-family: "Arimo", Arial, sans-serif;
    font-weight: 700;
    font-size: 32px;
    fill: var(--paper-white);
    letter-spacing: 1px;
  }
  .origin-box { fill: var(--label-black); stroke: var(--gold); stroke-width: 2.5; }
  .origin-text {
    font-family: "Arimo", Arial, sans-serif;
    font-weight: 700;
    font-size: 15px;
    fill: var(--paper-white);
  }
  .volume-text {
    font-family: "Arimo", Arial, sans-serif;
    font-weight: 700;
    font-size: 19px;
    fill: var(--gold-light);
  }
  .emblem-area { fill: url(#emblemGold); }
</style>
</head>
<body>
<main class="label-stage">
  <svg class="bottle-label" viewBox="0 0 800 760" xmlns="http://www.w3.org/2000/svg" aria-label="Orchardine wine spirit front label by Harbor Stillhouse">
    <defs>
      <linearGradient id="emblemGold" x1="0" y1="0" x2="1" y2="1">
        <stop offset="0" stop-color="#e2b862"/>
        <stop offset="1" stop-color="#8a5f25"/>
      </linearGradient>
      <path id="labelShape" d="M90,160 A70,70 0 0 0 160,90 Q400,5 640,90 A70,70 0 0 0 710,160 V650 A60,60 0 0 0 650,710 H150 A60,60 0 0 0 90,650 Z"/>
    </defs>

    <g class="ribbon-tails">
      <polygon class="ribbon-tail" points="120,515 30,530 60,580 10,625 120,610"/>
      <polyline class="ribbon-tail-line" points="120,528 52,540 78,580 45,612 120,600"/>
      <polygon class="ribbon-tail" points="680,495 770,510 740,560 790,605 680,590"/>
      <polyline class="ribbon-tail-line" points="680,508 748,520 722,560 755,592 680,580"/>
    </g>

    <use href="#labelShape" class="label-body"/>
    <use href="#labelShape" class="frame-white" transform="translate(400 390) scale(0.96) translate(-400 -390)" vector-effect="non-scaling-stroke"/>
    <use href="#labelShape" class="frame-gold" transform="translate(400 390) scale(0.925) translate(-400 -390)" vector-effect="non-scaling-stroke"/>
    <use href="#labelShape" class="frame-dots" transform="translate(400 390) scale(0.9) translate(-400 -390)" vector-effect="non-scaling-stroke"/>

    <ellipse class="emblem-area" cx="400" cy="112" rx="38" ry="42" role="img" aria-label="Gold apple emblem made of lettering"/>

    <g class="type-tag">
      <polygon class="tag-ends" points="270,176 318,176 318,216 270,216 280,196"/>
      <polygon class="tag-ends" points="530,176 482,176 482,216 530,216 520,196"/>
      <rect class="tag-box" x="300" y="177" width="200" height="38"/>
      <text class="tag-text" x="400" y="204" text-anchor="middle">WINE SPIRIT</text>
    </g>

    <text class="product-name" x="400" y="328" text-anchor="middle">Orchardine</text>
    <text class="tagline" x="400" y="392" text-anchor="middle">Handcrafted Distillery</text>
    <text class="established" x="400" y="445" text-anchor="middle">EST- 2018</text>

    <g class="maker-ribbon" transform="rotate(-3 400 552)">
      <rect class="ribbon-band" x="115" y="510" width="570" height="88"/>
      <rect class="ribbon-gold" x="128" y="521" width="544" height="66"/>
      <text class="maker-name" x="400" y="566" text-anchor="middle">HARBOR STILLHOUSE</text>
    </g>

    <rect class="origin-box" x="330" y="616" width="140" height="27"/>
    <text class="origin-text" x="400" y="635" text-anchor="middle">DENMARK</text>
    <text class="volume-text" x="400" y="676" text-anchor="middle">500 ML</text>
  </svg>
</main>
</body>
</html>
```